Infografik für Tanzschule
Zielgruppe
Wir sind eine Tanzschule für die Tänze Salsa, Bachata, kizomba & Zouk in Freiburg
Aufgabenstellung
DESIGN-BRIEFING
Tarifübersicht – Tanzschule Ritmo del Alba
Projektziel
Gestaltung einer klaren, hochwertigen Tarifübersicht für eine Tanzschule.
Die Grafik dient: als Information & Orientierung auf der Homepage, als visuelle Grundlage für das Anmeldeformular vor Ort, Der Einstieg erfolgt immer über eine gratis Schnupperstunde.
Die verbindliche Anmeldung erfolgt nach der Schnupperstunde vor Ort über ein Formular mit Auswahlkästchen.
Grundaufbau
3 Tarifkarten nebeneinander
Einheitlicher, moderner Stil
evtl. Emotionale Bilder (echte Tanzszenen, echte Menschen)
Klare Hierarchie:
Titel → Preis → Erklärung → Vorteile → Auswahlkästchen
Struktur der Tarifkarten
KARTE 1 – EINSTIEG
Titel: 1× PRO WOCHE TANZEN
Preis: 56 €/ 39 € erm.
Subline: pro Person · pro Kalendermonat
Vorteile (max. 4 Bulletpoints):
Ein fester wöchentlicher Kurs
Klare Routine & Struktur
Ausweichstunde im selben Monat möglich (muss klar enthalten sein)
Auswahl: ☐ 1× pro Woche tanzen
KARTE 2 – REGELMÄSSIG TANZEN (darf visuell leicht hervorgehoben sein, z. B. Rahmen oder Badge)
Optionales Badge:
SEHR BELIEBT
Titel: 2× PRO WOCHE TANZEN
Preis: 98 € / 68 € erm.
Vorteile:
Zwei feste wöchentliche Kurse
Mehr Praxis & schnellerer Fortschritt
Ausweichstunde im selben Monat möglich
Auswahl:
☐ 2× pro Woche tanzen
KARTE 3 – MAXIMALE FREIHEIT
Titel: FLAT – ALL YOU CAN DANCE
Preis: ab 129 € / 99 € erm.
Alle Tänze
Alle Kurse (für dein Tanz-Level)
Alle Workshops (für dein Tanz-Level)
Maximale Freiheit
☐ FLAT 1 Monat – 149 € | 119 € erm. (monatlich kündbar)
☐ FLAT 3 Monate – 129 € | 99 € erm. (3 Monate Erstlaufzeit)
Einheitlicher Hinweis unter den Karten (kleiner Text)
Ausweic..

```html
<!DOCTYPE html>
<html lang="de">
<head>
<meta charset="utf-8">
<title>Tarifübersicht – Ritmo del Alba</title>
<link rel="stylesheet" href="https://fonts.googleapis.com/css2?family=Nunito:wght@400;600;700;800&display=swap">
<style>
:root{
  --mint:#94d6bd;
  --lilac:#b29dd9;
  --berry:#b81e4f;
  --card-bg:#f2f2f2;
  --ink:#1f1f1f;
  --muted:#8a8a8a;
  --stage:#ffffff;
  --side:#efefef;
  --paper:#ffffff;
}
*{box-sizing:border-box;margin:0;padding:0}
html,body{width:1200px;height:675px;overflow:hidden}
body{font-family:"Nunito",sans-serif;color:var(--ink);background:var(--stage);position:relative}
.side{position:absolute;left:725px;top:0;width:475px;height:675px;background:var(--side)}

/* tariff card */
.card{position:absolute;width:198px;height:327px;background:var(--card-bg)}
.card-head{height:55px;padding:10px 0 0 18px;color:#fff;clip-path:polygon(9px 0,100% 0,100% 100%,0 100%,0 9px)}
.mint .card-head{background:var(--mint)}
.lilac .card-head{background:var(--lilac)}
.berry .card-head{background:var(--berry)}
.card-title{font-size:16.5px;font-weight:700;line-height:20px}
.card-sub{font-size:11px;line-height:14px;margin-top:5px;font-weight:400}
.card-body{padding:16px 7px 0 11px}
.price{display:flex;align-items:baseline;gap:7px;white-space:nowrap}
.price-amount{font-size:23px;font-weight:800;line-height:26px}
.price-unit{font-size:11.5px}
.price-reduced{font-size:8.6px;color:var(--muted);margin-top:4px;line-height:11px}
.perks{list-style:none;margin-top:13px}
.perks li{position:relative;padding-left:24px;font-size:11px;line-height:13px;margin-bottom:7px}
.perks svg{position:absolute;left:0;top:2px;width:10px;height:9px}
.mint .perks svg{stroke:var(--mint)}
.lilac .perks svg{stroke:var(--lilac)}
.berry .perks svg{stroke:var(--berry)}
.divider{position:absolute;left:11px;right:7px;top:211px;border-top:1px solid var(--ink)}
.options{position:absolute;left:11px;top:224px;right:7px}
.option{display:flex;gap:12px;font-size:11px;line-height:13px;margin-bottom:9px}
.box{flex:none;width:12px;height:12px;border:1px solid var(--ink);margin-top:0}
.badge{position:absolute;left:132px;top:264px;width:76px;height:76px;border-radius:50%;background:#fff;z-index:2;display:flex;align-items:center;justify-content:center}
.badge span{width:64px;height:64px;border-radius:50%;background:var(--lilac);color:#fff;font-size:10.5px;font-weight:600;line-height:12px;text-align:center;display:flex;align-items:center;justify-content:center;transform:rotate(10deg)}

/* registration form */
.form{position:absolute;left:776px;top:74px;width:372px;height:526px;background:var(--paper);font-size:5.6px;line-height:7.5px}
.form-title{position:absolute;left:27px;top:27px;font-size:12.5px;font-weight:700}
.brand{position:absolute;left:268px;top:22px;display:flex;align-items:center;gap:4px;font-size:9px;font-weight:600;color:var(--berry)}
.brand i{width:10px;height:10px;border-radius:50%;background:var(--berry);display:block}
.school{position:absolute;left:268px;top:58px;width:100px}
.school p{margin-bottom:7px}
.school b{font-weight:700}
.salutation{position:absolute;left:27px;top:57px;display:flex;gap:9px}
.mini-check{display:flex;align-items:center;gap:5px}
.mini-box{width:6px;height:6px;border:.6px solid var(--ink)}
.field{position:absolute;left:27px;width:211px;border-bottom:.6px solid var(--ink);height:9px}
.agree{position:absolute;left:27px}
.minis{position:absolute;left:27px;top:187px}
.minis .card{transform:scale(.525);transform-origin:top left}
.fine{position:absolute;left:27px;width:318px;font-size:4.2px;line-height:6.2px;color:var(--muted)}
.sepa-title{position:absolute;left:27px;top:397px;font-weight:600}
.line-field{position:absolute;left:27px;width:318px;border-bottom:.6px solid var(--ink);height:9px}
.start{position:absolute;left:27px;top:463px}
.months{display:flex;gap:4.3px;margin-top:4px;font-size:4.2px;line-height:6px}
.months div{width:8px;text-align:center}
.months .mini-box{margin:2px auto 0}
.sign{position:absolute;left:194px;top:463px;width:146px}
.sign small{display:block;font-size:4.2px;color:var(--muted);line-height:6px}
.sign-line{border-bottom:.6px solid var(--ink);margin-top:13px}
</style>
</head>
<body>
<svg width="0" height="0" style="position:absolute">
  <symbol id="tick" viewBox="0 0 10 9"><polyline points="1,4.5 4,7.5 9,1" fill="none" stroke-width="1.6"/></symbol>
</svg>

<section class="tariffs" aria-label="Tarifübersicht">
  <article class="card mint" style="left:58px;top:161px">
    <header class="card-head"><h2 class="card-title">Einstieg</h2><p class="card-sub">1× pro Woche tanzen</p></header>
    <div class="card-body">
      <div class="price"><span class="price-amount">€ 56,-</span><span class="price-unit">pro Person/Monat</span></div>
      <p class="price-reduced">€ 39,- ermäßigt pro Person/Monat</p>
      <ul class="perks">
        <li><svg><use href="#tick"/></svg>Ein fester wöchentlicher Kurs</li>
        <li><svg><use href="#tick"/></svg>Klare Routine &amp; Struktur</li>
        <li><svg><use href="#tick"/></svg>Ausweichstunde* im<br>selben Monat möglich</li>
      </ul>
    </div>
    <div class="divider"></div>
    <div class="options"><div class="option"><span class="box"></span>1× pro Woche tanzen</div></div>
  </article>

  <article class="card lilac" style="left:263px;top:161px">
    <header class="card-head"><h2 class="card-title">Regelmäßig Tanzen</h2><p class="card-sub">2× pro Woche tanzen</p></header>
    <div class="card-body">
      <div class="price"><span class="price-amount">€ 98,-</span><span class="price-unit">pro Person/Monat</span></div>
      <p class="price-reduced">€ 68,- ermäßigt pro Person/Monat</p>
      <ul class="perks">
        <li><svg><use href="#tick"/></svg>Zwei feste wöchentliche Kurse</li>
        <li><svg><use href="#tick"/></svg>Mehr Praxis &amp;<br>schnellerer Fortschritt</li>
        <li><svg><use href="#tick"/></svg>Ausweichstunde* im<br>selben Monat möglich</li>
      </ul>
    </div>
    <div class="divider"></div>
    <div class="options"><div class="option"><span class="box"></span>2× pro Woche tanzen</div></div>
    <div class="badge"><span>SEHR<br>BELIEBT</span></div>
  </article>

  <article class="card berry" style="left:468px;top:161px">
    <header class="card-head"><h2 class="card-title">Maximale Freiheit</h2><p class="card-sub">Flat – All you can dance.</p></header>
    <div class="card-body">
      <div class="price"><span class="price-amount">€ 129,-</span><span class="price-unit">pro Person/Monat</span></div>
      <p class="price-reduced">€ 99,- ermäßigt pro Person/Monat</p>
      <ul class="perks">
        <li><svg><use href="#tick"/></svg>Alle Tänze</li>
        <li><svg><use href="#tick"/></svg>Alle Kurse<br>(für dein Tanz-Level)</li>
        <li><svg><use href="#tick"/></svg>Alle Workshops<br>(für dein Tanz-Level)</li>
      </ul>
    </div>
    <div class="divider"></div>
    <div class="options">
      <div class="option"><span class="box"></span><span>FLAT 1 Monat<br>€ 149,- | € 119,- erm.<br>(monatlich kündbar)</span></div>
      <div class="option"><span class="box"></span><span>FLAT 3 Monate<br>€ 129,- | € 99,- erm.<br>(3 Monate Erstlaufzeit)</span></div>
    </div>
  </article>
</section>

<div class="side"></div>

<section class="form" aria-label="Anmeldeformular">
  <h1 class="form-title">Anmeldeformular</h1>
  <div class="brand"><i></i>Ritmo del Alba</div>
  <div class="school">
    <p><b>Tanzschule Ritmo del Alba</b><br>Lindenweg 14<br>79100 Talheim</p>
    <p><b>Geschäftsanschrift</b><br>Martin Kessler<br>Gartenstraße 8<br>79102 Talheim</p>
    <p><b>Kontakt</b><br>0151 23 456 789<br>kontakt@ritmo-del-alba.de<br>ritmo-del-alba.de</p>
  </div>
  <div class="salutation">
    <span class="mini-check"><span class="mini-box"></span>Frau</span>
    <span class="mini-check"><span class="mini-box"></span>Herr</span>
    <span class="mini-check"><span class="mini-box"></span>Div.</span>
  </div>
  <div class="field" style="top:72px">Vor- &amp; Nachname:</div>
  <div class="field" style="top:89px">Staße, Nr.:</div>
  <div class="field" style="top:107px">Plz, Ort:</div>
  <div class="field" style="top:124px">Telefon:</div>
  <div class="field" style="top:141px">E-Mail:</div>
  <div class="agree mini-check" style="top:159px"><span class="mini-box"></span>Ermäßigt (Student*in / Schüler*in / Auszubildende*r)</div>
  <div class="agree mini-check" style="top:170px"><span class="mini-box"></span>Ja, ich möchte den Newsletter und Kursinformationen erhalten.</div>

  <div class="minis">
    <article class="card mint" style="left:0;top:0">
      <header class="card-head"><h2 class="card-title">Einstieg</h2><p class="card-sub">1× pro Woche tanzen</p></header>
      <div class="card-body">
        <div class="price"><span class="price-amount">€ 56,-</span><span class="price-unit">pro Person/Monat</span></div>
        <p class="price-reduced">€ 39,- ermäßigt pro Person/Monat</p>
        <ul class="perks">
          <li><svg><use href="#tick"/></svg>Ein fester wöchentlicher Kurs</li>
          <li><svg><use href="#tick"/></svg>Klare Routine &amp; Struktur</li>
          <li><svg><use href="#tick"/></svg>Ausweichstunde* im<br>selben Monat möglich</li>
        </ul>
      </div>
      <div class="divider"></div>
      <div class="options"><div class="option"><span class="box"></span>1× pro Woche tanzen</div></div>
    </article>
    <article class="card lilac" style="left:107.5px;top:0">
      <header class="card-head"><h2 class="card-title">Regelmäßig Tanzen</h2><p class="card-sub">2× pro Woche tanzen</p></header>
      <div class="card-body">
        <div class="price"><span class="price-amount">€ 98,-</span><span class="price-unit">pro Person/Monat</span></div>
        <p class="price-reduced">€ 68,- ermäßigt pro Person/Monat</p>
        <ul class="perks">
          <li><svg><use href="#tick"/></svg>Zwei feste wöchentliche Kurse</li>
          <li><svg><use href="#tick"/></svg>Mehr Praxis &amp;<br>schnellerer Fortschritt</li>
          <li><svg><use href="#tick"/></svg>Ausweichstunde* im<br>selben Monat möglich</li>
        </ul>
      </div>
      <div class="divider"></div>
      <div class="options"><div class="option"><span class="box"></span>2× pro Woche tanzen</div></div>
      <div class="badge"><span>SEHR<br>BELIEBT</span></div>
    </article>
    <article class="card berry" style="left:215px;top:0">
      <header class="card-head"><h2 class="card-title">Maximale Freiheit</h2><p class="card-sub">Flat – All you can dance.</p></header>
      <div class="card-body">
        <div class="price"><span class="price-amount">€ 129,-</span><span class="price-unit">pro Person/Monat</span></div>
        <p class="price-reduced">€ 99,- ermäßigt pro Person/Monat</p>
        <ul class="perks">
          <li><svg><use href="#tick"/></svg>Alle Tänze</li>
          <li><svg><use href="#tick"/></svg>Alle Kurse<br>(für dein Tanz-Level)</li>
          <li><svg><use href="#tick"/></svg>Alle Workshops<br>(für dein Tanz-Level)</li>
        </ul>
      </div>
      <div class="divider"></div>
      <div class="options">
        <div class="option"><span class="box"></span><span>FLAT 1 Monat<br>€ 149,- | € 119,- erm.<br>(monatlich kündbar)</span></div>
        <div class="option"><span class="box"></span><span>FLAT 3 Monate<br>€ 129,- | € 99,- erm.<br>(3 Monate Erstlaufzeit)</span></div>
      </div>
    </article>
  </div>

  <p class="fine" style="top:367px">Verlängerung &amp; Kündigung: Der Vertrag verlängert sich automatisch um jeweils einen Monat und ist mit 14 Tagen Frist zum Monatsende kündbar. Ausnahme „FLAT 3 Monate“ kündbar nach Ablauf der Erstlaufzeit.<br>*Ausweichstunde: im selben Kalendermonat möglich.</p>
  <p class="sepa-title">Einzugsermächtigung / SEPA-Lastschriftmandat</p>
  <p class="fine" style="top:405px">Ich ermächtige Ritmo del Alba, Zahlungen von meinem Konto per Lastschrift einzuziehen und mein Kreditinstitut, diese Lastschriften einzulösen. Bei Ablehnung der Lastschrift fallen Kosten von 10,00 € pro Rückbuchung an. Ich kann innerhalb von acht Wochen ab Belastungsdatum die Erstattung verlangen. Gemäß der Bedingung meines Kreditinstituts. Die Kursgebühr wird im ersten Monat zur Mitte/Ende eingezogen, danach jeweils zum 05. jenes Monats.</p>
  <div class="line-field" style="top:430px">Kreditinsitut:</div>
  <div class="line-field" style="top:446px">IBAN:</div>
  <div class="start">Kursstart / Anmeldung ab:
    <div class="months">
      <div>Jan<span class="mini-box"></span></div><div>Feb<span class="mini-box"></span></div><div>Mrz<span class="mini-box"></span></div><div>Apr<span class="mini-box"></span></div><div>Mai<span class="mini-box"></span></div><div>Jun<span class="mini-box"></span></div><div>Jul<span class="mini-box"></span></div><div>Aug<span class="mini-box"></span></div><div>Sep<span class="mini-box"></span></div><div>Okt<span class="mini-box"></span></div><div>Nov<span class="mini-box"></span></div><div>Dez<span class="mini-box"></span></div>
    </div>
  </div>
  <div class="sign">Datum / Unterschrift:<small>Wir verweisen auf unsere umseitig abgedruckten AGB</small><div class="sign-line"></div></div>
</section>
</body>
</html>
```